Marwick barber salon has created a lotion and needs help titling.Loma by marwick ?Marwi

The product is for a lotion bottle , my prototype lotion bottle size is an 8oz black lotion bottle with pump. I want the label in florescent green. It should tap into the emotion of potential buyers. The design should say choose me 😀(not literally ). Though the text should be clear and punchy . I.e " the skin multi-vitamin." I'm looking for a designer intrigued by the thought of my lotion. The label should be georgeous,informative, with visuals that immediately convey what my product is and how it works.Not distracting, but clear and punchy, with no expectation of someone to read more than a couple of words.The text should support the visual in a way the visual could not. It seems that nowadays visuals are taking over with very little text. The font,color , or punch of color should be enticing.
So here are some particular ideas of points about the lotion that could possibly be put on back as is done by lotion makers.
.ingredients
.ZNT approved
.portion of proceeds go to bright path fund
.TC circled ( which is for pending trademark)
. I would like the word New in fluorescent on the bottle
.P.O Box address of place of manufacturing product.
. To help skin stay slightly moist,soft,and flexible with a smooth fine grained texture.

its a lotion so I want it available for all

Barber

9bcb3c

• the word" Loma" and By marwick...the word new on the bottle visible

```html
<!DOCTYPE html>
<html lang="en">
<head>
<meta charset="utf-8">
<title>Loma by Marwick – Lotion Label</title>
<link rel="stylesheet" href="https://fonts.googleapis.com/css2?family=Montserrat:wght@500;700;800&display=swap">
<style>
  :root {
    --backdrop: #ecedeb;
    --label-white: #f7f8f6;
    --brand-green: #7ab51d;
    --text-green: #6ea520;
    --fluoro-green: #9bcb3c;
    --wave-pale: #b7d77c;
    --wave-light: #94c23f;
    --wave-mid: #78ad28;
    --wave-deep: #64991f;
    --sun-orange: #e9a11a;
    --white: #ffffff;
  }
  * { margin: 0; padding: 0; box-sizing: border-box; }
  html, body { width: 1000px; height: 1200px; overflow: hidden; }
  body {
    position: relative;
    background: radial-gradient(ellipse at 50% 40%, #fafafa 0%, var(--backdrop) 75%);
    font-family: "Montserrat", Arial, sans-serif;
  }
  .label {
    position: absolute;
    left: 290px;
    top: 400px;
    width: 420px;
    height: 640px;
    border-radius: 30px;
    overflow: hidden;
    background: var(--label-white);
    box-shadow: 0 10px 30px rgba(0,0,0,0.08);
  }
  .label-waves { position: absolute; inset: 0; }
  .new-tag {
    position: absolute;
    top: 58px;
    left: 50%;
    transform: translateX(-50%);
    padding: 6px 18px;
    border-radius: 20px;
    background: var(--fluoro-green);
    color: var(--white);
    font-weight: 800;
    font-size: 16px;
    letter-spacing: 3px;
  }
  .brand {
    position: absolute;
    top: 128px;
    left: 0;
    width: 100%;
    text-align: center;
  }
  .brand-row {
    display: inline-flex;
    align-items: center;
    gap: 12px;
  }
  .brand-name {
    font-weight: 500;
    font-size: 104px;
    line-height: 1;
    letter-spacing: -3px;
    color: var(--brand-green);
  }
  .brand-dot {
    width: 30px;
    height: 30px;
    border-radius: 50%;
    background: var(--sun-orange);
    margin-top: -44px;
  }
  .brand-by {
    position: absolute;
    top: 242px;
    left: 74px;
    font-weight: 700;
    font-size: 15px;
    color: var(--sun-orange);
  }
  .headline {
    position: absolute;
    top: 282px;
    width: 100%;
    text-align: center;
    font-weight: 700;
    font-size: 21px;
    color: var(--text-green);
  }
  .blurb {
    position: absolute;
    top: 316px;
    left: 62px;
    width: 296px;
    font-weight: 700;
    font-size: 11.5px;
    line-height: 1.45;
    text-align: justify;
    text-align-last: center;
    color: var(--text-green);
  }
  .claim {
    position: absolute;
    top: 500px;
    width: 100%;
    text-align: center;
    font-weight: 700;
    font-size: 19px;
    line-height: 1.7;
    color: var(--white);
  }
  .net-weight {
    position: absolute;
    top: 592px;
    width: 100%;
    text-align: center;
    font-weight: 500;
    font-size: 16px;
    color: var(--white);
  }
</style>
</head>
<body>
  <main class="label">
    <svg class="label-waves" viewBox="0 0 420 640" width="420" height="640" aria-hidden="true">
      <path d="M0 362 Q210 430 420 382 L420 640 L0 640 Z" fill="var(--wave-pale)"/>
      <path d="M0 398 Q210 440 420 400 L420 640 L0 640 Z" fill="var(--wave-light)"/>
      <path d="M0 415 Q200 455 420 432 L420 640 L0 640 Z" fill="var(--wave-mid)"/>
      <path d="M0 470 Q210 482 420 468 L420 640 L0 640 Z" fill="var(--wave-deep)"/>
    </svg>

    <span class="new-tag">NEW</span>

    <div class="brand">
      <div class="brand-row">
        <span class="brand-name">Loma</span>
        <span class="brand-dot"></span>
      </div>
    </div>
    <p class="brand-by">BY MARWICK</p>

    <h1 class="headline">THE SKIN MULTI-VITAMIN</h1>
    <p class="blurb">Vitamin-rich care that helps skin stay slightly moist, soft and flexible with a smooth, fine grained texture.</p>

    <p class="claim">KEEPS SKIN SOFT,<br>SMOOTH AND SLIGHTLY MOIST</p>
    <p class="net-weight">Net Weight: 8oz</p>
  </main>
</body>
</html>
```